CD cover and poster

We are looking for a designer to design a CD cover together with a poster.

Target Market(s)

classical music lovers

Industry/Entity Type

musik

Font styles to use
Other font styles liked:
• Lexend Tera

Requirements
Must have
• cd cover and poster with a similar design

```html
<!DOCTYPE html>
<html lang="en">
<head>
<meta charset="utf-8">
<title>Quasi Una Fantasia – Classical Piano Concert</title>
<link rel="stylesheet" href="https://fonts.googleapis.com/css2?family=Lexend+Tera:wght@400;500&family=Montserrat:wght@400;500&family=Allura&display=swap">
<style>
  :root {
    --paper: #ffffff;
    --night: #141110;
    --gold: #d7a85e;
    --ivory: #f4efe8;
  }
  * { margin: 0; padding: 0; box-sizing: border-box; }
  html, body {
    width: 878px;
    height: 1200px;
    overflow: hidden;
    background: var(--paper);
  }
  .poster {
    position: absolute;
    left: 14px;
    top: 14px;
    width: 850px;
    height: 1172px;
    background: var(--night);
    overflow: hidden;
    font-family: "Montserrat", sans-serif;
    color: var(--ivory);
  }
  .portrait {
    position: absolute;
    inset: 0;
    background:
      radial-gradient(ellipse 40% 34% at 80% 30%, rgba(176,118,72,0.75), rgba(90,60,40,0.35) 55%, transparent 80%),
      radial-gradient(ellipse 55% 30% at 72% 58%, rgba(58,42,32,0.8), transparent 80%),
      linear-gradient(100deg, #1b1614 0%, #2a211c 30%, #3d2c22 55%, #2a1f19 75%, #161211 100%);
  }
  .shade {
    position: absolute;
    inset: 0;
    background: linear-gradient(180deg, rgba(20,17,16,0.55) 0%, transparent 18%, transparent 50%, rgba(20,17,16,0.85) 70%, rgba(20,17,16,0.95) 100%);
  }
  h1, h2 { font-weight: inherit; }
  .kicker {
    position: absolute;
    top: 68px;
    left: 156px;
    font-family: "Lexend Tera", sans-serif;
    font-size: 17px;
    letter-spacing: 2px;
    color: var(--gold);
    white-space: nowrap;
  }
  .live {
    position: absolute;
    top: 346px;
    left: 136px;
    font-family: "Lexend Tera", sans-serif;
    font-size: 19px;
    letter-spacing: 1px;
    white-space: nowrap;
  }
  .performer-first {
    position: absolute;
    top: 398px;
    left: 268px;
    font-size: 44px;
    font-weight: 400;
    white-space: nowrap;
  }
  .performer-last {
    position: absolute;
    top: 450px;
    left: 72px;
    font-family: "Lexend Tera", sans-serif;
    font-size: 70px;
    font-weight: 500;
    letter-spacing: 1px;
    white-space: nowrap;
  }
  .programme-title {
    position: absolute;
    top: 720px;
    left: 88px;
    font-family: "Allura", cursive;
    font-size: 94px;
    color: var(--gold);
    white-space: nowrap;
  }
  .programme-intro {
    position: absolute;
    top: 852px;
    left: 92px;
    width: 140px;
    font-family: "Lexend Tera", sans-serif;
    font-size: 12px;
    line-height: 24px;
    text-align: center;
    color: var(--gold);
  }
  .programme-works {
    position: absolute;
    top: 852px;
    left: 416px;
    width: 400px;
    font-family: "Lexend Tera", sans-serif;
    font-size: 12px;
    line-height: 28px;
    text-align: center;
    white-space: nowrap;
  }
  .details {
    position: absolute;
    top: 1040px;
    left: 94px;
    font-family: "Lexend Tera", sans-serif;
    font-size: 34px;
    letter-spacing: 2px;
    color: var(--gold);
    white-space: nowrap;
  }
  .details .place { position: absolute; left: 274px; }
</style>
</head>
<body>
  <main class="poster">
    <div class="portrait" role="img" aria-label="Warm-lit photograph of the pianist in a dark jacket, looking over his shoulder, beside a wooden wall"></div>
    <div class="shade"></div>

    <p class="kicker">CLASSICAL PIANO CONCERT</p>
    <p class="live">LIVE PERFORMANCE</p>
    <h1>
      <span class="performer-first">Adrian</span>
      <span class="performer-last">VELMOR</span>
    </h1>

    <h2 class="programme-title">Quasi Una Fantasia</h2>
    <p class="programme-intro">with well known<br>piano works by</p>
    <p class="programme-works">Harlow (Fantasy in C minor),<br>Brennick (Nocturne Sonata),<br>Castell (Rover Fantasy),<br>Dovrin (Fantasy in F minor) and<br>Ellery (Night Rider Fantasy)</p>

    <p class="details"><span class="date">DATE</span><span class="place">YOUR PLACE</span></p>
  </main>
</body>
</html>
```